Online Consultancy Needs a New Logo & Business Card Design

Based on the new logo we just received from another contest here on Maketrove,

You'll find a few different versions of our logo as well as examples of business card designs we like in this folder:
==> https://share.plumvault.net/folderview?id=7Kq2WzTn4pLrXcv9BsHaYe1MoD5g&usp=sharing

We are considering two options:
- clean, black design
- clean, white/blue design

We're willing to consider both options.

We're considering adding some special effects to the cards when printing - emboss, rounded corners, etc.

However, please deliver a design WITHOUT round corners.

Target Market(s)

Successful business people, serious and older audience.

Industry/Entity Type

Business

Contact Information for Business Card

For the business card, I would like a minimalistic card with the logo on one side (perhaps in the middle) and the contact information on the other.

For the contact information please use:
Name: Peter Lund
Position: Founder
Email: peter.lund@korvim.com
Phone Number: +381 63 98 76 210
Website URL: www.korvim.com

Font styles to use
Serif
Sans Serif

Requirements
Must have
• Must fit in perfectly with our current website design.

```html
<!DOCTYPE html>
<html lang="en">
<head>
<meta charset="utf-8">
<title>Korvim Business Card</title>
<link rel="stylesheet" href="https://fonts.googleapis.com/css2?family=Montserrat:wght@400;600&display=swap">
<style>
  :root {
    --page-bg: #e9eaec;
    --card-white: #ffffff;
    --card-grey: #e2e3e5;
    --brand-blue: #00adef;
    --swoosh-dark: #2e2d2f;
    --text-white: #ffffff;
  }
  * { box-sizing: border-box; margin: 0; padding: 0; }
  html, body {
    width: 1200px; height: 900px; overflow: hidden;
    background: var(--page-bg);
  }
  .business-card {
    position: absolute; left: 180px; top: 210px;
    width: 840px; height: 480px;
    overflow: hidden;
    box-shadow: 0 14px 40px rgba(0,0,0,.18);
    font-family: "Montserrat", sans-serif;
    font-variant: small-caps;
  }
  .card-art { position: absolute; inset: 0; }
  .brand-name {
    position: absolute; left: 0; right: 0; top: 96px;
    text-align: center;
    font-size: 62px; font-weight: 400; letter-spacing: 1px;
    font-variant: normal;
    color: var(--brand-blue);
    text-transform: lowercase;
  }
  .identity {
    position: absolute; right: 430px; top: 300px;
    text-align: right; color: var(--text-white);
    letter-spacing: 1.5px;
  }
  .person-name { font-size: 18px; font-weight: 600; }
  .person-role { font-size: 14px; margin-top: 6px; }
  .address { font-size: 15px; margin-top: 32px; line-height: 1.5; }
  .divider {
    position: absolute; left: 430px; top: 262px;
    width: 1px; height: 176px; background: var(--text-white); opacity: .8;
  }
  .contact-list {
    position: absolute; left: 450px; top: 250px;
    list-style: none; color: var(--text-white);
    font-size: 15px; letter-spacing: 1.5px;
  }
  .contact-list li { display: flex; align-items: center; gap: 8px; height: 24px; white-space: nowrap; }
  .contact-list li.web-line { font-size: 13px; letter-spacing: 1px; }
  .contact-list li.gap-before { margin-top: 22px; }
  .contact-icon { width: 15px; height: 15px; flex: none; }
</style>
</head>
<body>
  <div class="business-card">
    <svg class="card-art" viewBox="0 0 840 480" width="840" height="480">
      <defs>
        <linearGradient id="paper" x1="0" y1="0" x2="0" y2="1">
          <stop offset="0" stop-color="var(--card-white)"/>
          <stop offset="1" stop-color="var(--card-grey)"/>
        </linearGradient>
      </defs>
      <rect class="paper" width="840" height="480" fill="url(#paper)"/>
      <path class="swoosh" d="M0,318 C250,232 560,166 840,122 C560,174 250,252 0,336 Z" fill="var(--swoosh-dark)"/>
      <path class="blue-band" d="M0,336 C250,252 560,174 840,132 L840,480 L0,480 Z" fill="var(--brand-blue)"/>
    </svg>

    <div class="brand-name">korvim</div>

    <div class="identity">
      <div class="person-name">Peter Lund</div>
      <div class="person-role">Founder</div>
      <div class="address">Suite # 14, Vela Tower,<br>Novi Grad 21000</div>
    </div>

    <div class="divider"></div>

    <ul class="contact-list">
      <li>
        <svg class="contact-icon" viewBox="0 0 16 16"><circle cx="8" cy="8" r="8" fill="#fff"/><path d="M5 4.5l2 0.5-0.5 2 2.5 2.5 2-0.5 0.5 2c-3 1.5-7.5-3-6.5-6.5z" fill="var(--brand-blue)"/></svg>
        +381 63 98 76 210
      </li>
      <li>
        <svg class="contact-icon" viewBox="0 0 16 16"><circle cx="8" cy="8" r="8" fill="#fff"/><rect x="5.5" y="3.5" width="5" height="9" rx="1" fill="var(--brand-blue)"/></svg>
        +381 11 40 52 318
      </li>
      <li>
        <svg class="contact-icon" viewBox="0 0 16 16"><circle cx="8" cy="8" r="8" fill="#fff"/><rect x="4" y="6" width="8" height="5" fill="var(--brand-blue)"/><rect x="5.5" y="4" width="5" height="2" fill="var(--brand-blue)"/></svg>
        +381 11 40 52 319
      </li>
      <li class="web-line gap-before">
        <svg class="contact-icon" viewBox="0 0 16 16"><circle cx="8" cy="8" r="8" fill="#fff"/><rect x="4" y="5" width="8" height="6" fill="var(--brand-blue)"/><path d="M4 5l4 3.5 4-3.5" stroke="#fff" fill="none"/></svg>
        peter.lund@korvim.com
      </li>
      <li class="web-line">
        <svg class="contact-icon" viewBox="0 0 16 16"><circle cx="8" cy="8" r="8" fill="#fff"/><circle cx="8" cy="8" r="4.5" fill="none" stroke="var(--brand-blue)"/><path d="M3.5 8h9M8 3.5v9" stroke="var(--brand-blue)"/></svg>
        www.korvim.com
      </li>
    </ul>
  </div>
</body>
</html>
```